Vantage Automotive Reconditioning Business Card

We need a professional business card that features our logo, a picture of the employee, and a brief list of our services.
I've attached a logo, and will attach photos at a later date.
The four services that need to be listed are Bumper repair and repainting, road rash repair, clear coat scratch repair, and automotive touch-up.
Target Market(s)
30 - 40 year male general managers of automobile dealerships. They are used to seeing every vendor gimmick under the sun. This brochure needs to impress with its simplicity and honesty.
Industry/Entity Type
Automotive
Look and feel
Each slider illustrates characteristics of the customer's brand and the style your logo design should communicate.

```html
<!DOCTYPE html>
<html lang="en">
<head>
<meta charset="utf-8">
<title>Vantage Automotive Reconditioning – Business Card</title>
<link href="https://fonts.googleapis.com/css2?family=Open+Sans:wght@400;600;700&display=swap" rel="stylesheet">
<style>
  :root {
    --page-bg: #e9e7e4;
    --card-white: #ffffff;
    --card-grey: #e4e4e4;
    --brand-red: #e0070f;
    --brand-red-deep: #9c0006;
    --charcoal: #333333;
    --stripe: #3a3a3a;
    --text-dark: #2c2c2c;
    --photo-light: #cfcfcf;
    --photo-dark: #9a9a9a;
  }
  * { box-sizing: border-box; margin: 0; padding: 0; }
  html, body { width: 1200px; height: 1000px; overflow: hidden; }
  body {
    background: var(--page-bg);
    font-family: "Open Sans", Arial, sans-serif;
    position: relative;
  }
  .card {
    position: absolute;
    left: 170px;
    width: 860px;
    height: 430px;
    border-radius: 28px;
    overflow: hidden;
    background: radial-gradient(ellipse at 45% 40%, var(--card-white) 0%, var(--card-grey) 100%);
    box-shadow: 0 10px 26px rgba(0,0,0,0.18);
  }
  .card--front { top: 50px; }
  .card--back { top: 520px; }

  /* Front */
  .front-logo {
    position: absolute;
    left: 0; right: 0; top: 130px;
    text-align: center;
    color: var(--charcoal);
    font-weight: 700;
  }
  .logo-name { font-size: 86px; line-height: 1; letter-spacing: 2px; text-transform: uppercase; }
  .logo-tagline { font-size: 24px; letter-spacing: 3px; text-transform: uppercase; margin-top: 6px; }
  .front-band {
    position: absolute;
    left: 0; right: 0; bottom: 0;
    height: 70px;
    background: linear-gradient(90deg, var(--brand-red-deep), var(--brand-red) 30%, var(--brand-red) 70%, var(--brand-red-deep));
    border-top: 8px solid var(--stripe);
    display: flex; align-items: center; justify-content: center;
  }
  .website { color: #fff; font-size: 22px; letter-spacing: 0.5px; }

  /* Back */
  .photo-slot {
    position: absolute;
    left: 70px; top: 40px;
    width: 250px; height: 218px;
    background: linear-gradient(180deg, var(--photo-light), var(--photo-dark));
    border-radius: 4px 4px 0 0;
  }
  .contact {
    position: absolute;
    left: 470px; top: 42px;
    color: var(--text-dark);
  }
  .contact-name { font-size: 30px; font-weight: 700; line-height: 1.15; text-transform: uppercase; }
  .contact-title { font-size: 28px; font-weight: 400; line-height: 1.15; text-transform: uppercase; }
  .contact-list { list-style: none; margin-top: 22px; }
  .contact-item { display: flex; align-items: center; gap: 12px; font-size: 19px; margin-bottom: 10px; }
  .contact-icon { width: 28px; height: 28px; flex: none; }
  .back-band {
    position: absolute;
    left: 0; right: 0; bottom: 0;
    height: 172px;
    background: linear-gradient(90deg, var(--brand-red-deep), var(--brand-red) 35%, var(--brand-red) 75%, var(--brand-red-deep));
    border-top: 8px solid var(--stripe);
  }
  .back-logo {
    position: absolute;
    left: 60px; top: 38px;
    color: #fff;
    font-weight: 700;
  }
  .back-logo .logo-name { font-size: 66px; }
  .back-logo .logo-tagline { font-size: 18px; letter-spacing: 2.5px; }
  .services {
    position: absolute;
    left: 500px; top: 22px;
    color: #fff;
    font-size: 20px;
    line-height: 1.55;
    text-transform: uppercase;
    list-style: none;
  }
  .services li { position: relative; padding-left: 22px; }
  .services li::before {
    content: "";
    position: absolute; left: 0; top: 12px;
    width: 8px; height: 8px; border-radius: 50%;
    background: #1a1a1a;
  }
</style>
</head>
<body>

<section class="card card--front" aria-label="Card front">
  <div class="front-logo">
    <div class="logo-name">Vantage</div>
    <div class="logo-tagline">Automotive Reconditioning</div>
  </div>
  <div class="front-band">
    <span class="website">www.yourwebsite.com</span>
  </div>
</section>

<section class="card card--back" aria-label="Card back">
  <div class="photo-slot" role="img" aria-label="Employee portrait photo placeholder"></div>

  <div class="contact">
    <p class="contact-name">Your Name Here</p>
    <p class="contact-title">Your Title</p>
    <ul class="contact-list">
      <li class="contact-item">
        <svg class="contact-icon" viewBox="0 0 28 28" aria-hidden="true">
          <circle cx="14" cy="14" r="13" fill="#e0070f" stroke="#9c0006" stroke-width="1.5"/>
          <rect x="10" y="7" width="8" height="14" rx="1.5" fill="#fff"/>
          <rect x="11.5" y="9" width="5" height="6" fill="#e0070f"/>
        </svg>
        <span>(+61) 04 5550 1827</span>
      </li>
      <li class="contact-item">
        <svg class="contact-icon" viewBox="0 0 28 28" aria-hidden="true">
          <circle cx="14" cy="14" r="13" fill="#e0070f" stroke="#9c0006" stroke-width="1.5"/>
          <rect x="7" y="9" width="14" height="10" fill="#fff"/>
          <path d="M7 9 L14 15 L21 9" fill="none" stroke="#e0070f" stroke-width="1.5"/>
        </svg>
        <span>sales@vantagerecon.com.au</span>
      </li>
    </ul>
  </div>

  <div class="back-band">
    <div class="back-logo">
      <div class="logo-name">Vantage</div>
      <div class="logo-tagline">Automotive Reconditioning</div>
    </div>
    <ul class="services">
      <li>Bumper repair and repainting</li>
      <li>Clear coat scratch repair</li>
      <li>And automotive touch-up.</li>
      <li>Road rash repair</li>
    </ul>
  </div>
</section>

</body>
</html>
```